Birch Hollow Lodge & Harbour. A site that will sell our lifestyle and embody our vision.

We are after a fun interactive website for our property development.
Check out our ideas for layout and content.
Use stock videos and phots if we havent provide enough.
Ive attached our Logo.
We are easy to reach and work with. Love the crative process.1.Our Vision.. (This clicks through to vision page)
Nestled in the North East corner of Tesla Lake , Sk amidst thousands of acres of natural beauty, a unique community is taking shape. A community that connectS people, nature and play. A place to find those simpler times.

2.Explore..(This clicks through to explore page)
Discover a new life of adventure, on the lake fishing, in the bush on our trail system or maybe the local golf course.

3. Live Here..(This through to Live page)
Birch Hollow has everything you need to start living a full life based in a thriving community.
Slow down and get to know nature and your neighbors

Target Market(s)

35-65 Lake Life

Coding

Coded - Design and coding required

Number of Pages Required

5+ page

Font styles to use
Other font styles liked:
• Anntonio

Colors
00AB8E
00BBA5
67D7C9
C6EFE9
E9F9F6
F0912C
F2A743
F7CA91
FBE8D2
FDF5EE

Requirements
Nice to have
• Interactive

```html
<!DOCTYPE html>
<html lang="en">
<head>
<meta charset="utf-8">
<title>Birch Hollow Lodge &amp; Harbour</title>
<link rel="stylesheet" href="https://fonts.googleapis.com/css2?family=Antonio:wght@400;600;700&family=Poppins:wght@300;400;500;600&family=Great+Vibes&display=swap">
<style>
:root{
  --green:#00AB8E;
  --green-2:#00BBA5;
  --mint:#67D7C9;
  --mint-pale:#C6EFE9;
  --mint-wash:#E9F9F6;
  --forest:#0f3b33;
  --forest-deep:#0b2a25;
  --ink:#1d1d1d;
  --body:#555d5b;
  --white:#ffffff;
  --head:'Antonio',sans-serif;
  --text:'Poppins',sans-serif;
  --script:'Great Vibes',cursive;
}
*{box-sizing:border-box;margin:0;padding:0}
html,body{width:1200px;height:3968px;overflow:hidden}
body{position:relative;background:var(--white);font-family:var(--text);color:var(--ink)}
.abs{position:absolute}
.btn{position:absolute;display:flex;align-items:center;gap:8px;justify-content:center;height:34px;padding:0 16px;font:500 11px/1 var(--text);letter-spacing:.08em;text-transform:uppercase;border:1.5px solid var(--green);color:var(--green);background:transparent}
.btn.light{border-color:var(--white);color:var(--white)}
.eyebrow{font:500 14px/1 var(--text);color:var(--green)}
.heading{font:600 30px/1.25 var(--head);color:var(--ink)}
.copy{font:400 12.5px/1.75 var(--text);color:var(--body)}
.copy+.copy{margin-top:14px}

/* hero */
.hero{left:0;top:0;width:1200px;height:620px;background:linear-gradient(180deg,#6f8f95 0%,#557e74 40%,#2f5e4a 70%,#1f4a3a 100%)}
.hero-shade{left:0;top:0;width:1200px;height:620px;background:linear-gradient(90deg,rgba(10,30,25,.55) 0%,rgba(10,30,25,.1) 55%,rgba(0,0,0,0) 100%)}
.topbar{left:760px;top:0;width:440px;height:30px;background:var(--green);display:flex;align-items:center;gap:24px}
.reserve{background:var(--white);color:var(--ink);font:600 10px/1 var(--text);letter-spacing:.06em;height:30px;width:160px;display:flex;align-items:center;justify-content:center}
.phone{display:flex;align-items:center;gap:8px;color:var(--white);font:500 11px/1 var(--text)}
.brand-tab{left:140px;top:0;width:68px;height:150px;background:var(--green);display:flex;align-items:flex-end;justify-content:center;padding-bottom:14px}
.brand-tab span{font:700 11px/1.15 var(--head);color:var(--white);text-align:center;letter-spacing:.05em;text-transform:uppercase}
.nav{left:480px;top:52px;display:flex}
.nav a{display:block;padding:8px 18px;font:400 12px/1 var(--text);color:var(--white);text-decoration:none}
.nav a.active{background:var(--green)}
.nav-rule{left:208px;top:100px;width:852px;height:1px;background:rgba(255,255,255,.35)}
.hero-welcome{left:140px;top:200px;font:400 40px/1 var(--script);color:var(--white)}
.hero-name{left:140px;top:250px;font:700 46px/1 var(--head);color:var(--green);letter-spacing:.04em;text-transform:uppercase}
.hero-sub{left:140px;top:308px;font:400 42px/1 var(--head);color:var(--white)}
.hero-copy{left:140px;top:370px;width:390px;font:400 11px/1.7 var(--text);color:rgba(255,255,255,.9)}

/* about */
.about-square{left:48px;top:900px;width:200px;height:300px;background:var(--green)}
.about-photo-a{left:80px;top:784px;width:240px;height:400px;background:linear-gradient(160deg,#8a6b4c,#5e4634 55%,#3b3f3a)}
.about-photo-b{left:336px;top:760px;width:264px;height:400px;background:linear-gradient(180deg,#dfe9f1 0%,#9fb3c2 40%,#3fa9b9 62%,#4d5d52 100%)}
.about-text{left:620px;top:806px;width:520px}
.about-text .heading{margin:12px 0 20px}

/* bands */
.peaks{left:0;width:1200px;background:linear-gradient(180deg,#ffffff 0%,#eef3f6 35%,#c9d7e0 65%,#e7eef2 100%)}
.explore{left:0;top:1512px;width:1200px;height:360px;background:linear-gradient(180deg,#174a40 0%,var(--forest) 50%,var(--forest-deep) 100%);text-align:center;color:var(--white)}
.explore h2{position:absolute;left:0;right:0;top:70px;font:600 36px/1 var(--head)}
.explore .tag{position:absolute;left:0;right:0;top:122px;font:500 13px/1 var(--text)}
.explore .lead{position:absolute;left:330px;width:540px;top:154px;font:400 12.5px/1.8 var(--text);color:rgba(255,255,255,.85)}

/* vision */
.vision-title{left:0;width:1200px;top:1968px;text-align:center;font:600 32px/1 var(--head)}
.vision-eyebrow{left:0;width:1200px;top:2024px;text-align:center}
.sketch{left:0;top:2320px;width:600px;height:360px;background:linear-gradient(180deg,rgba(246,248,248,0) 0%,#f3f6f5 60%,#f7f9f8 100%)}
.vision-frame{left:992px;top:2096px;width:160px;height:384px;background:var(--green)}
.vision-photo{left:592px;top:2120px;width:560px;height:440px;background:linear-gradient(180deg,#c6d6dd 0%,#7c9a92 35%,#3d6f63 55%,#4f9fa0 75%,#2f5e58 100%)}
.vision-card{left:140px;top:2088px;width:548px;height:400px;background:var(--white);box-shadow:0 10px 40px rgba(0,0,0,.14);padding:36px 40px}
.vision-card .heading{font-size:28px;margin-bottom:20px}
.vision-card .copy{font-size:13px;line-height:1.9;width:450px}

/* live here */
.live-frame-a{left:120px;top:2760px;width:200px;height:220px;background:var(--green)}
.live-frame-b{left:180px;top:2840px;width:412px;height:312px;border:2px solid var(--green)}
.live-photo{left:140px;top:2788px;width:400px;height:324px;background:linear-gradient(180deg,#e9a46b 0%,#b9805f 30%,#5c5e63 60%,#2f3f4a 100%)}
.play{left:310px;top:2920px;width:60px;height:60px;border-radius:50%;background:var(--white);display:flex;align-items:center;justify-content:center}
.live-text{left:620px;top:2816px;width:520px}
.live-text .heading{margin:12px 0 22px}

/* footer */
.treeline{left:0;top:3290px;width:1200px;height:300px;background:linear-gradient(180deg,#ffffff 0%,#dfe8ec 30%,#7d9a93 70%,var(--forest-deep) 100%)}
.footer{left:0;top:3580px;width:1200px;height:388px;background:var(--forest-deep);color:var(--white)}
.foot-brand{left:140px;top:40px;width:160px;height:210px;display:flex;align-items:flex-end;justify-content:center;padding-bottom:18px}
.foot-brand span{font:700 24px/1.15 var(--head);text-align:center;text-transform:uppercase;letter-spacing:.05em}
.foot-col h4{font:600 22px/1 var(--head);margin-bottom:22px}
.foot-col .title-rule{width:40px;height:2px;background:var(--green);margin:-12px 0 18px}
.links{display:grid;grid-template-columns:110px 110px;row-gap:12px;font:400 11.5px/1 var(--text);color:rgba(255,255,255,.85)}
.contact dt{font:600 11.5px/1 var(--text);margin-bottom:6px}
.contact dd{font:400 11px/1.5 var(--text);color:rgba(255,255,255,.8);margin-bottom:12px}
.news{display:flex;width:220px;height:30px}
.news .field{flex:1;background:var(--white);font:400 10px/30px var(--text);color:#999;padding-left:10px}
.news .go{width:44px;background:var(--green);font:600 11px/30px var(--text);text-align:center}
.social{display:flex;gap:12px;margin-top:22px}
.social i{display:block;width:26px;height:26px;border-radius:50%;border:1.5px solid rgba(255,255,255,.7)}
.foot-rule{left:140px;top:322px;width:920px;height:1px;background:rgba(255,255,255,.2)}
.copyright{left:0;width:1200px;top:352px;text-align:center;font:400 11px/1 var(--text);color:rgba(255,255,255,.75)}
</style>
</head>
<body>

<!-- Hero -->
<section class="abs hero" role="img" aria-label="Photo of a green mountain lake with a small boat under steep forested peaks"></section>
<div class="abs hero-shade"></div>
<div class="abs brand-tab"><span>Birch<br>Hollow</span></div>
<div class="abs topbar">
  <div class="reserve">RESERVE YOUR ROOM</div>
  <div class="phone">
    <svg width="12" height="12" viewBox="0 0 24 24"><path fill="#fff" d="M6.6 10.8a15.1 15.1 0 0 0 6.6 6.6l2.2-2.2a1 1 0 0 1 1-.25 11.4 11.4 0 0 0 3.6.57 1 1 0 0 1 1 1V20a1 1 0 0 1-1 1A17 17 0 0 1 3 4a1 1 0 0 1 1-1h3.5a1 1 0 0 1 1 1c0 1.25.2 2.45.57 3.57a1 1 0 0 1-.25 1z"/></svg>
    +1 (306) 555-0148
  </div>
</div>
<nav class="abs nav">
  <a class="active">Home</a><a>About Us</a><a>Our Vision</a><a>Explore</a><a>Live Here</a><a>Contact</a>
</nav>
<div class="abs nav-rule"></div>
<div class="abs hero-welcome">Welcome to</div>
<div class="abs hero-name">Birch Hollow</div>
<div class="abs hero-sub">Resort Luxury</div>
<p class="abs hero-copy">A quiet lakeside retreat where forest trails, calm water and friendly neighbours come together. Wake to misty mornings, spend the day on the lake and end it by the fire under open northern skies.</p>
<div class="btn light" style="left:140px;top:470px;width:144px">Learn More
  <svg width="12" height="8" viewBox="0 0 12 8"><path d="M0 4h10M7 1l3 3-3 3" stroke="#fff" fill="none" stroke-width="1.3"/></svg></div>

<!-- About -->
<div class="abs about-square"></div>
<div class="abs about-photo-a" role="img" aria-label="Photo of a lodge terrace with wooden deck chairs"></div>
<div class="abs about-photo-b" role="img" aria-label="Photo of a hiker seated above a turquoise mountain lake"></div>
<div class="abs about-text">
  <div class="eyebrow">About Us</div>
  <h2 class="heading">Lorem Ipsum is simply dummy text of the printing and typesetting industry.</h2>
  <p class="copy">Lorem Ipsum is simply dummy text of the printing and typesetting industry. Lorem Ipsum has been the industry's standard dummy text ever since the 1500s, when an unknown printer took a galley of type and scrambled it to make a type specimen book. It has survived not only five centuries, but also the leap into electronic typesetting, remaining essentially unchanged.</p>
  <p class="copy">Lorem Ipsum is simply dummy text of the printing and typesetting industry. Lorem Ipsum has been the industry's standard dummy text ever since the 1500s, when an unknown printer took a galley of type and scrambled it to make a type specimen book.</p>
</div>
<div class="btn" style="left:620px;top:1164px;width:144px">Learn More
  <svg width="12" height="8" viewBox="0 0 12 8"><path d="M0 4h10M7 1l3 3-3 3" stroke="#00AB8E" fill="none" stroke-width="1.3"/></svg></div>

<div class="abs peaks" style="top:1220px;height:292px" role="img" aria-label="Soft illustration of snowy mountain peaks"></div>

<!-- Explore -->
<section class="abs explore" role="region" aria-label="Explore">
  <h2>Explore</h2>
  <div class="tag">It Is A Long Established Fact That A Reader Will Be Distracted By The Readable</div>
  <p class="lead">Discover A New Life Of Adventure, On The Lake Fishing, In The Bush On Our Trail System Or Maybe The Local Golf Course.</p>
  <div class="btn light" style="left:528px;top:232px;width:144px">Learn More
    <svg width="12" height="8" viewBox="0 0 12 8"><path d="M0 4h10M7 1l3 3-3 3" stroke="#fff" fill="none" stroke-width="1.3"/></svg></div>
</section>

<!-- Vision -->
<h2 class="abs vision-title">Lorem Ipsum is simply</h2>
<div class="abs eyebrow vision-eyebrow">Our Vision</div>
<div class="abs sketch" role="img" aria-label="Faint line sketch of a cabin among pine trees"></div>
<div class="abs vision-frame"></div>
<div class="abs vision-photo" role="img" aria-label="Photo of a couple on a lakeshore dock below mountains"></div>
<div class="abs vision-card">
  <h3 class="heading">Lorem Ipsum is simply dummy text of the printing and typesetting industry.</h3>
  <p class="copy">Nestled in the North East corner of Tamsin Lake, amidst thousands of acres of natural beauty, a unique community is taking shape. A community that connects people, nature and play. A place to find those simpler times.</p>
  <div class="btn" style="left:40px;top:320px;width:144px">Learn More
    <svg width="12" height="8" viewBox="0 0 12 8"><path d="M0 4h10M7 1l3 3-3 3" stroke="#00AB8E" fill="none" stroke-width="1.3"/></svg></div>
</div>

<!-- Live Here -->
<div class="abs live-frame-a"></div>
<div class="abs live-frame-b"></div>
<div class="abs live-photo" role="img" aria-label="Video still of friends relaxing by a pool at sunset"></div>
<div class="abs play"><svg width="18" height="20" viewBox="0 0 18 20"><path d="M2 1l15 9-15 9z" fill="#1d1d1d"/></svg></div>
<div class="abs live-text">
  <div class="eyebrow">Live Here</div>
  <h2 class="heading">Lorem Ipsum is simply dummy text of the printing and typesetting industry.</h2>
  <p class="copy" style="font-size:13px">Birch Hollow has everything you need to start living a full life based in a thriving community.<br>Slow down and get to know nature and your neighbors</p>
  <p class="copy" style="font-size:13px">It is a long established fact that a reader will be distracted by the readable content of a page when looking at its layout.</p>
</div>
<div class="btn" style="left:620px;top:3170px;width:144px">Learn More
  <svg width="12" height="8" viewBox="0 0 12 8"><path d="M0 4h10M7 1l3 3-3 3" stroke="#00AB8E" fill="none" stroke-width="1.3"/></svg></div>

<!-- Footer -->
<div class="abs treeline" role="img" aria-label="Illustration of misty mountains above a dark pine forest"></div>
<footer class="abs footer">
  <div class="abs foot-brand"><span>Birch<br>Hollow</span></div>
  <div class="abs foot-col" style="left:332px;top:48px">
    <h4>Quick Link</h4><div class="title-rule"></div>
    <div class="links"><span>Home</span><span>Our Vision</span><span>About Us</span><span>Live Here</span><span>Explore</span><span>Contact</span></div>
  </div>
  <div class="abs foot-col contact" style="left:572px;top:48px">
    <h4>Contact Info</h4><div class="title-rule"></div>
    <dl>
      <dt>Phone</dt><dd>+1 (306) 555-0148</dd>
      <dt>Address</dt><dd>Address line 1, Address line 2<br>Address line 3</dd>
      <dt>Email</dt><dd>hello@birchhollowlodge.com</dd>
    </dl>
  </div>
  <div class="abs foot-col" style="left:832px;top:48px">
    <h4>Follow Us</h4><div class="title-rule"></div>
    <div class="news"><div class="field">Enter your email</div><div class="go">GO</div></div>
    <div class="social"><i></i><i></i><i></i><i></i></div>
  </div>
  <div class="abs foot-rule"></div>
  <div class="abs copyright">© 2022 Birch Hollow Lodge &amp; Harbour. All Right Reserved.</div>
</footer>

</body>
</html>
```